Winelabel for Italian Wine incl. box.

Front and back label for new Italian wine.
It´s a premium redwine,
Size of Labels: Front 100x115 | Back 60x85
For front label we can also use these sizes:
95X115 - 100x100 – 86x97 – 100x110
For back labels : 60X90 – 60X95 – 60X100
We can only use one type of foil finishing.
BRAND = FIORALBA dal` Colle Brisco (in 2 lines)
2. titel = Calice di Sera
Semi lines = Ancient vinification Traditions | Truscany
Style = elegant Italian coloured Harlequin,
Other colors using white/black/gold
Include a round "water-mark" with text : Selected for loyal winelowers
Back label will be short story + legal data + barcode.
Outer box of 6 bottles case design print on all 4 fronts.

```html
<!DOCTYPE html>
<html lang="en">
<head>
<meta charset="utf-8">
<title>FIORALBA dal` Colle Brisco – Wine Labels</title>
<link rel="stylesheet" href="https://fonts.googleapis.com/css2?family=Italiana&family=Cormorant+Garamond:wght@400;500&family=Josefin+Sans:wght@300;400&display=swap">
<style>
  :root {
    --paper: #e8e3dc;
    --paper-back: #e5e0d9;
    --coral: #e8665a;
    --plum: #86334a;
    --teal: #39686a;
    --blush: #dfc3bb;
    --ink: #2b2020;
    --green: #2aa05a;
    --page: #ffffff;
  }
  * { margin: 0; padding: 0; box-sizing: border-box; }
  html, body { width: 1200px; height: 2823px; overflow: hidden; background: var(--page); }
  .sheet { position: relative; width: 1200px; height: 2823px; }

  .brand-dot { position: absolute; left: 50%; transform: translateX(-50%); border-radius: 50%; background: var(--plum); }
  .brand-name, .brand-sub, .wine-title, .tagline, .spec, .story, .cell-title { position: absolute; left: 0; width: 100%; text-align: center; }
  .brand-name { font-family: "Italiana", serif; color: var(--coral); letter-spacing: 2px; line-height: 1; }
  .brand-sub { font-family: "Cormorant Garamond", serif; color: var(--ink); line-height: 1; }

  /* Front label */
  .front-label { position: absolute; left: 0; top: 0; width: 1200px; height: 1381px; background: var(--paper); overflow: hidden; }
  .front-label .brand-dot { top: 50px; width: 100px; height: 100px; }
  .front-label .brand-name { top: 172px; font-size: 76px; }
  .front-label .brand-sub { top: 252px; font-size: 42px; }
  .wine-title { top: 360px; font-family: "Cormorant Garamond", serif; font-size: 48px; color: var(--teal); }
  .tagline { top: 424px; font-family: "Josefin Sans", sans-serif; font-weight: 400; font-size: 28px; color: var(--ink); }
  .harlequin-field {
    position: absolute; left: 0; top: 512px; width: 1200px; height: 869px;
    background: linear-gradient(180deg, var(--plum) 0%, var(--teal) 30%, var(--coral) 55%, var(--teal) 78%, var(--plum) 100%);
  }

  /* Size notes */
  .spec { font-family: "Josefin Sans", sans-serif; font-weight: 300; font-size: 58px; }
  .spec-front { top: 1518px; color: var(--green); }
  .spec-back { top: 1598px; color: var(--ink); }
  .arrow { position: absolute; left: 540px; width: 120px; height: 72px; }
  .arrow-up { top: 1410px; }
  .arrow-down { top: 1682px; }

  /* Back label */
  .back-label { position: absolute; left: 207px; top: 1799px; width: 795px; height: 1021px; background: var(--paper-back); }
  .back-label .brand-dot { top: 42px; width: 90px; height: 90px; }
  .back-label .brand-name { top: 164px; font-size: 58px; }
  .back-label .brand-sub { top: 228px; font-size: 36px; }
  .bottle-motif {
    position: absolute; left: 66px; top: 268px; width: 660px; height: 236px;
    background: linear-gradient(90deg, var(--plum) 0%, var(--blush) 30%, var(--ink) 50%, var(--blush) 70%, var(--plum) 100%);
    opacity: .85;
  }
  .story { left: 69px; width: auto; text-align: left; top: 538px; font-family: "Josefin Sans", sans-serif; font-size: 26px; color: var(--ink); }
  .rule { position: absolute; left: 69px; height: 0; border-top: 2px dotted var(--ink); }
  .legal-box { position: absolute; left: 69px; top: 719px; width: 599px; height: 239px; border: 3px solid var(--ink); display: flex; }
  .legal-cell { position: relative; flex: 1; }
  .legal-cell + .legal-cell { border-left: 3px solid var(--ink); }
  .cell-title { top: 24px; font-family: "Josefin Sans", sans-serif; font-size: 28px; color: var(--ink); }
</style>
</head>
<body>
<main class="sheet">

  <section class="front-label">
    <div class="brand-dot"></div>
    <h1 class="brand-name">FIORALBA</h1>
    <p class="brand-sub">dal` Colle Brisco</p>
    <h2 class="wine-title">Calice di Sera</h2>
    <p class="tagline">Ancient vinification Traditions | Truscany</p>
    <div class="harlequin-field" role="img" aria-label="Harlequin pattern of coral, plum, teal, blush and black diamond shapes"></div>
  </section>

  <svg class="arrow arrow-up" viewBox="0 0 120 72" aria-hidden="true">
    <polygon points="60,0 112,36 84,36 84,72 36,72 36,36 8,36" fill="var(--green)"/>
  </svg>
  <p class="spec spec-front">front label 100x115</p>
  <p class="spec spec-back">back label 60x85</p>
  <svg class="arrow arrow-down" viewBox="0 0 120 72" aria-hidden="true">
    <polygon points="36,0 84,0 84,36 112,36 60,72 8,36 36,36" fill="var(--ink)"/>
  </svg>

  <section class="back-label">
    <div class="brand-dot"></div>
    <h1 class="brand-name">FIORALBA</h1>
    <p class="brand-sub">dal` Colle Brisco</p>
    <div class="bottle-motif" role="img" aria-label="Two plum wine bottles flanking a small harlequin motif"></div>
    <p class="story">short story:</p>
    <div class="rule" style="top:560px; left:230px; width:438px;"></div>
    <div class="rule" style="top:604px; width:599px;"></div>
    <div class="rule" style="top:647px; width:599px;"></div>
    <div class="rule" style="top:691px; width:560px;"></div>
    <div class="legal-box">
      <div class="legal-cell"><p class="cell-title">legal data</p></div>
      <div class="legal-cell"><p class="cell-title">barcode.</p></div>
    </div>
  </section>

</main>
</body>
</html>
```